Need a book cover design for a Pagelume Book

Book has a long title and sub title so lots of words to fit on the cover.

I can be flexible a bit with the sub title due to the length of it but ideally i can get a design that takes everything.

Here is the title:

Stellar Chemistry: The Roots of Reactions, Bonding, and Crystal Growth

Sub Title/Heading
A Newcomer's Tour of Organic Synthesis, Polymer Design, Lattice Models, and Enzyme Catalysis

```html
<!DOCTYPE html>
<html lang="en">
<head>
<meta charset="utf-8">
<title>Stellar Chemistry – Book Cover</title>
<link rel="stylesheet" href="https://fonts.googleapis.com/css2?family=Bebas+Neue&family=Oswald:wght@600&family=Montserrat:wght@400;600;700&display=swap">
<style>
  :root {
    --backdrop: #000000;
    --paper: #fde2e3;
    --magenta: #c80e62;
    --ink: #111111;
    --rule: #b4615f;
    --accent-green: #0bb04f;
  }
  html, body {
    margin: 0;
    padding: 0;
    width: 1200px;
    height: 1200px;
    overflow: hidden;
    background: var(--backdrop);
  }
  .canvas {
    position: relative;
    width: 1200px;
    height: 1200px;
    background: var(--backdrop);
  }
  .cover {
    position: absolute;
    left: 240px;
    top: 58px;
    width: 720px;
    height: 1080px;
    background: var(--paper);
    overflow: hidden;
  }
  .spine-bar {
    position: absolute;
    background: var(--magenta);
  }
  .spine-bar--top { left: 146px; top: 0; width: 23px; height: 98px; }
  .spine-bar--main { left: 418px; top: 443px; width: 23px; height: 637px; }
  .title {
    position: absolute;
    left: 0;
    top: 0;
    width: 720px;
    height: 460px;
  }
  .title text {
    font-family: "Bebas Neue", "Oswald", sans-serif;
    fill: var(--magenta);
  }
  .subtitle {
    position: absolute;
    left: 61px;
    top: 448px;
    margin: 0;
    font-family: "Oswald", sans-serif;
    font-weight: 600;
    font-size: 49px;
    line-height: 58px;
    letter-spacing: -1.5px;
    text-transform: uppercase;
    color: var(--magenta);
  }
  .subtitle span { display: block; }
  .divider {
    position: absolute;
    left: 61px;
    top: 751px;
    width: 116px;
    height: 2px;
    background: var(--rule);
  }
  .tagline {
    position: absolute;
    left: 61px;
    top: 774px;
    margin: 0;
    font-family: "Montserrat", sans-serif;
    font-weight: 400;
    font-size: 21px;
    line-height: 27.5px;
    color: var(--ink);
  }
  .tagline strong { font-weight: 700; }
  .tagline span { display: block; }
  .author {
    position: absolute;
    left: 61px;
    top: 981px;
    margin: 0;
    font-family: "Montserrat", sans-serif;
    font-weight: 600;
    font-size: 26px;
    letter-spacing: 1.6px;
    color: var(--ink);
  }
  .emblem {
    position: absolute;
    left: 506px;
    top: 735px;
    width: 168px;
    height: 190px;
    border-radius: 50%;
    background: radial-gradient(circle at 50% 50%, var(--accent-green) 0 12%, #e9a3bf 13% 45%, var(--paper) 72%);
  }
</style>
</head>
<body>
<div class="canvas">
  <main class="cover">
    <div class="spine-bar spine-bar--top"></div>

    <svg class="title" viewBox="0 0 720 460" aria-label="Stellar Chemistry">
      <text x="60" y="262" font-size="224" textLength="600" lengthAdjust="spacingAndGlyphs">STELLAR</text>
      <text x="60" y="432" font-size="224" textLength="600" lengthAdjust="spacingAndGlyphs">CHEMISTRY</text>
    </svg>

    <div class="spine-bar spine-bar--main"></div>

    <h2 class="subtitle">
      <span>The Roots</span>
      <span>of Reactions,</span>
      <span>Bonding, and</span>
      <span>Crystal Growth</span>
    </h2>

    <div class="divider"></div>

    <p class="tagline">
      <span>A Newcomer's Tour of</span>
      <span><strong>Organic Synthesis, Polymer</strong></span>
      <span><strong>Design, Lattice Models,</strong></span>
      <span>and <strong>Enzyme Catalysis</strong></span>
    </p>

    <p class="author">AUTHOR NAME</p>

    <div class="emblem" role="img" aria-label="Atom emblem with orbiting electrons around a green nucleus"></div>
  </main>
</div>
</body>
</html>
```